Varlow Business Partners
Business Cards & Stationery
Professional
Thomas E. Varlow
CEO
58 Birch Lane, North
Suite 318
Edgeton, NJ 07415
thomas.varlow@varlowbp.com
Back of card should contain the black version of the logo - no other information

```html
<!DOCTYPE html>
<html lang="en">
<head>
<meta charset="utf-8">
<title>Varlow Business Partners – Business Cards</title>
<link href="https://fonts.googleapis.com/css2?family=Source+Sans+3:wght@400;600;700&display=swap" rel="stylesheet">
<style>
  :root {
    --stage: #3b3c3f;
    --orange: #f07a1e;
    --orange-deep: #e0650f;
    --paper: #ffffff;
    --ink: #2b2b2b;
    --ink-soft: #3a3a3a;
    --rule: #b9b9b9;
    --logo-grey: #6d6e71;
  }
  * { box-sizing: border-box; margin: 0; padding: 0; }
  html, body { width: 1200px; height: 852px; overflow: hidden; }
  body {
    background: var(--stage);
    font-family: "Source Sans 3", "Myriad Pro", Arial, sans-serif;
    position: relative;
  }
  .card {
    position: absolute;
    width: 560px;
    height: 340px;
    border-radius: 22px;
    overflow: hidden;
    background: var(--paper);
  }
  .card--front-a { left: 110px; top: 70px; }
  .card--front-b { left: 530px; top: 442px; }
  .card__shape { position: absolute; inset: 0; width: 100%; height: 100%; }
  .card__content { position: absolute; inset: 0; color: var(--ink); }

  .contact-name { font-weight: 700; font-size: 21px; line-height: 1.1; }
  .contact-role { font-size: 15px; margin-top: 4px; }
  .contact-address { font-size: 15px; line-height: 1.3; }
  .contact-line { font-size: 15px; display: flex; align-items: center; gap: 8px; line-height: 1.5; }
  .contact-line svg { width: 14px; height: 14px; flex: none; }

  .brand { position: absolute; display: flex; align-items: center; gap: 12px; }
  .brand__dot { width: 30px; height: 30px; border-radius: 50%; background: var(--orange); flex: none; }
  .brand__name {
    color: var(--logo-grey);
    font-weight: 600;
    font-size: 22px;
    line-height: 1.05;
    text-transform: uppercase;
    letter-spacing: 0.5px;
  }

  /* front A: orange left */
  .card--front-a .identity { position: absolute; left: 36px; top: 44px; }
  .card--front-a .contact-address { position: absolute; left: 36px; top: 160px; }
  .card--front-a .contact-list { position: absolute; left: 36px; top: 264px; }
  .card--front-a .brand { left: 330px; top: 60px; }

  /* front B: orange right */
  .card--front-b .identity { position: absolute; right: 36px; top: 44px; text-align: right; }
  .card--front-b .contact-address { position: absolute; right: 36px; top: 120px; text-align: right; }
  .card--front-b .contact-list { position: absolute; right: 36px; top: 264px; }
  .card--front-b .contact-line { justify-content: flex-end; }
  .card--front-b .brand { left: 36px; top: 120px; }
</style>
</head>
<body>

  <section class="card card--front-a" aria-label="Business card, orange left">
    <svg class="card__shape" viewBox="0 0 560 340" aria-hidden="true">
      <path d="M0 0 H300 C230 110 360 210 292 340 H0 Z" fill="var(--orange)"/>
      <path d="M314 0 C244 110 374 210 306 340" fill="none" stroke="var(--rule)" stroke-width="5"/>
    </svg>
    <div class="card__content">
      <div class="identity">
        <div class="contact-name">Thomas E. Varlow</div>
        <div class="contact-role">CEO</div>
      </div>
      <div class="contact-address">
        58 Birch Lane, North<br>Suite 318<br>Edgeton, NJ 07415
      </div>
      <div class="contact-list">
        <div class="contact-line">
          <svg viewBox="0 0 16 16"><path d="M4 1l3 3-2 2c1 2 3 4 5 5l2-2 3 3-2 3C7 15 1 9 1 3z" fill="var(--ink)"/></svg>
          908.555.0142
        </div>
        <div class="contact-line">
          <svg viewBox="0 0 16 16"><rect x="1" y="3" width="14" height="10" fill="var(--ink)"/><path d="M1 3l7 6 7-6" fill="none" stroke="var(--orange)" stroke-width="1.4"/></svg>
          thomas.varlow@varlowbp.com
        </div>
      </div>
      <div class="brand">
        <span class="brand__dot"></span>
        <span class="brand__name">Varlow<br>Business<br>Partners</span>
      </div>
    </div>
  </section>

  <section class="card card--front-b" aria-label="Business card, orange right">
    <svg class="card__shape" viewBox="0 0 560 340" aria-hidden="true">
      <path d="M560 0 H300 C230 80 340 200 312 340 H560 Z" fill="var(--orange)"/>
      <path d="M286 0 C216 80 326 200 298 340" fill="none" stroke="var(--rule)" stroke-width="5"/>
    </svg>
    <div class="card__content">
      <div class="brand">
        <span class="brand__dot"></span>
        <span class="brand__name">Varlow<br>Business<br>Partners</span>
      </div>
      <div class="identity">
        <div class="contact-name">Thomas E. Varlow</div>
        <div class="contact-role">CEO</div>
      </div>
      <div class="contact-address">
        58 Birch Lane, North<br>Suite 318<br>Edgeton, NJ 07415
      </div>
      <div class="contact-list">
        <div class="contact-line">
          908.555.0142
          <svg viewBox="0 0 16 16"><path d="M4 1l3 3-2 2c1 2 3 4 5 5l2-2 3 3-2 3C7 15 1 9 1 3z" fill="var(--ink)"/></svg>
        </div>
        <div class="contact-line">
          thomas.varlow@varlowbp.com
          <svg viewBox="0 0 16 16"><rect x="1" y="3" width="14" height="10" fill="var(--ink)"/><path d="M1 3l7 6 7-6" fill="none" stroke="var(--orange)" stroke-width="1.4"/></svg>
        </div>
      </div>
    </div>
  </section>

</body>
</html>
```